Designing of Orientation Materials and Innovative Ways to ‘Market’ Procurement Function

To Market and promote Procurement function and it’s ‘real’ capabilities clearly, to demonstrate that the function is an enabler instead being perceive as a barrier to other internal functions. Sometimes due to the lack of a common language even makes it difficult for other functions (e.g) Marketing and Procurement to understand each other’s aims and intentions.
The audience could be from all functions such as; Human Resource, Finance, Sales & Marketing, Supply Chain/Procurement, Corporate Affairs and Information System.

```html
<!DOCTYPE html>
<html lang="en">
<head>
<meta charset="utf-8">
<title>Procurement's Evolving Value Proposition</title>
<link rel="stylesheet" href="https://fonts.googleapis.com/css2?family=Barlow:wght@400;600&family=Barlow+Condensed:wght@400;700&family=Barlow+Semi+Condensed:wght@700&display=swap">
<style>
  :root {
    --ink: #45474b;
    --ink-soft: #55575b;
    --legend: #9a9ca0;
    --value: #e0602e;
    --demand: #e6c93a;
    --tco: #62a853;
    --price: #626399;
    --supply: #d7366f;
    --spine: #7a3a1e;
    --art-light: #f25a4a;
    --art-mid: #d01a12;
    --art-dark: #8a1410;
  }
  html, body { margin: 0; padding: 0; overflow: hidden; }
  body { width: 1200px; height: 1200px; }
  .canvas {
    position: relative; width: 1200px; height: 1200px; overflow: hidden;
    background: radial-gradient(ellipse at 20% 20%, #ffffff 0%, #f4f4f4 55%, #ebebeb 100%);
    color: var(--ink);
    font-family: "Barlow", sans-serif;
  }
  .title {
    position: absolute; left: 54px; top: 42px; margin: 0;
    font-family: "Barlow Condensed", sans-serif; font-weight: 400;
    font-size: 80px; line-height: 82px; letter-spacing: -0.5px; color: var(--ink);
    transform: scaleX(0.9); transform-origin: left top;
  }
  .title strong { font-weight: 700; display: block; }
  .title span { display: block; }
  .graphic { position: absolute; left: 0; top: 0; width: 1200px; height: 1200px; }
  .stage { position: absolute; }
  .stage h2 {
    position: absolute; margin: 0; white-space: nowrap;
    font-family: "Barlow Semi Condensed", sans-serif; font-weight: 700;
    font-size: 30px; line-height: 1; color: var(--ink);
  }
  .stage p {
    position: absolute; margin: 0; white-space: nowrap;
    font-size: 15.5px; line-height: 22px; color: var(--ink-soft);
  }
  .stage b { font-weight: 600; color: var(--ink); }
  .right h2 { left: 0; }
  .left h2 { right: 0; }
  .left p { right: 0; text-align: right; }
  .tag { display: inline-block; }
  .right .tag { width: 45px; text-align: right; margin-right: 8px; }
  .legend {
    position: absolute; left: 1021px; top: 1141px;
    font-family: "Barlow Condensed", sans-serif; font-weight: 700;
    font-size: 13px; color: var(--legend); line-height: 26px;
  }
  .legend div { display: flex; align-items: center; }
  .legend i {
    font-style: normal; display: inline-flex; align-items: center; justify-content: center;
    width: 20px; height: 20px; border: 1px solid #c9cacc; border-radius: 50%;
    font-size: 10px; margin-right: 2px;
  }
</style>
</head>
<body>
<main class="canvas">
  <h1 class="title"><strong>PROCUREMENT’S</strong><span>EVOLVING VALUE</span><span>PROPOSITION</span></h1>

  <svg class="graphic" viewBox="0 0 1200 1200">
    <defs>
      <linearGradient id="artFill" x1="0" x2="1" y1="0" y2="1">
        <stop offset="0" stop-color="var(--art-light)"/>
        <stop offset="0.55" stop-color="var(--art-mid)"/>
        <stop offset="1" stop-color="var(--art-dark)"/>
      </linearGradient>
    </defs>

    <rect class="art-placeholder" x="565" y="236" width="76" height="136" fill="url(#artFill)" opacity="0.85" role="img" aria-label="Illustration: red arrow fletching at the top of the arrow"/>

    <line class="timeline-spine" x1="603" y1="372" x2="603" y2="890" stroke="var(--spine)" stroke-width="5"/>

    <rect class="art-placeholder" x="267" y="890" width="668" height="262" fill="url(#artFill)" opacity="0.85" role="img" aria-label="Illustration: red and white archery target with the arrow in the bullseye"/>

    <line x1="603" y1="446" x2="888" y2="446" stroke="var(--value)" stroke-width="3"/>
    <line x1="269" y1="534" x2="603" y2="534" stroke="var(--demand)" stroke-width="3"/>
    <line x1="603" y1="622" x2="962" y2="622" stroke="var(--tco)" stroke-width="3"/>
    <line x1="312" y1="709" x2="603" y2="709" stroke="var(--price)" stroke-width="3"/>
    <line x1="603" y1="797" x2="874" y2="797" stroke="var(--supply)" stroke-width="3"/>

    <circle cx="600" cy="446" r="8.5" fill="var(--value)"/>
    <circle cx="600" cy="534" r="8.5" fill="var(--demand)"/>
    <circle cx="600" cy="622" r="8.5" fill="var(--tco)"/>
    <circle cx="600" cy="709" r="8.5" fill="var(--price)"/>
    <circle cx="600" cy="797" r="8.5" fill="var(--supply)"/>
  </svg>

  <section class="stage right" style="left:625px;top:412px;">
    <h2>VALUE MANAGEMENT</h2>
    <p style="top:45px;left:-4px;"><b class="tag">VP:</b>Increase business value direved from spend</p>
    <p style="top:67px;left:-4px;"><b class="tag">RoP:</b>Trusted business advisor and change agent</p>
  </section>

  <section class="stage left" style="right:635px;top:494px;">
    <h2>DEMAND MANAGEMENT</h2>
    <p style="top:52px;"><b>VP:</b>&nbsp;&nbsp; Reduce demand activity, complexity and variability</p>
    <p style="top:74px;"><b>RoP:</b> Spend/budget consultant and relationship manager</p>
  </section>

  <section class="stage right" style="left:618px;top:593px;">
    <h2>TOTAL COST OF OWNERSHIP</h2>
    <p style="top:41px;left:3px;"><b class="tag">VP:</b>Shift from lower price to TCO</p>
    <p style="top:63px;left:3px;"><b class="tag">RoP:</b>Supply expert, team leader, project manager</p>
  </section>

  <section class="stage left" style="right:635px;top:677px;">
    <h2>PRICE</h2>
    <p style="top:51px;"><b>VP:</b>&nbsp; Right goods and services at the right price</p>
    <p style="top:73px;"><b>RoP:</b>&nbsp; Negotiator</p>
  </section>

  <section class="stage right" style="left:618px;top:764px;">
    <h2>SUPPLY ASSURANCE</h2>
    <p style="top:48px;left:3px;"><b class="tag">VP:</b>Right gods/sercices at the right time and place</p>
    <p style="top:70px;left:3px;"><b class="tag" style="text-align:left;margin-left:-6px;width:51px;">RoP:</b>Buyer/Planner</p>
  </section>

  <aside class="legend">
    <div><i>VP</i>= VALUE PROPOSITION</div>
    <div><i>RoP</i>= ROLE OF PROCUREMENT</div>
  </aside>
</main>
</body>
</html>
```